Package Card - Horse Products

I require a card design for the top of a package (see photo). This product is a number holder that gets pinned on to a horse bridle or saddle blanket for competitions. It is a high quality, genuine leather, and premium product.Card is 15cm across and 6cm high. Requirements:Must have - Logo, -"Equestrian Number Holder"- Place on back for barcodeAnything else is up to you! Suggestions and ideas welcome. Card back colour can be any colour.My outcome is for it to look like a premium product

Target Market(s)

High end equestrian competitors

Colors
fbf289

Requirements
Must have
• Logo
• "Equestrian Number Holder"
• "Genuine Leather"
• Room on the back for a barcode sticker
Nice to have
• Should look up market and elegant

```html
<!DOCTYPE html>
<html lang="en">
<head>
<meta charset="utf-8">
<title>Tide Hollow Equestrian – Equestrian Number Holder</title>
<link rel="stylesheet" href="https://fonts.googleapis.com/css2?family=Rokkitt:wght@600;700&family=Montserrat:wght@800&display=swap">
<style>
  :root {
    --gold-top: #dba524;
    --gold-mid: #fddc02;
    --gold-bottom: #e7b51b;
    --ink: #0b0b0b;
    --logo-gold: #d9a640;
    --number-gold: #f6c915;
    --ornament-tone: #8a6a10;
  }
  html, body {
    margin: 0;
    padding: 0;
    overflow: hidden;
    background: #ffffff;
  }
  .card {
    position: relative;
    width: 1200px;
    height: 480px;
    overflow: hidden;
    background: linear-gradient(180deg, var(--gold-top) 0%, var(--gold-mid) 52%, var(--gold-bottom) 100%);
  }
  .card-frame {
    position: absolute;
    inset: 7px;
    border: 3px solid var(--ink);
  }
  .logo-panel {
    position: absolute;
    left: 389px;
    top: 0;
    width: 419px;
    height: 196px;
    background: var(--ink);
    display: flex;
    align-items: center;
    justify-content: center;
    gap: 16px;
  }
  .logo-name {
    font-family: "Rokkitt", serif;
    font-weight: 600;
    color: var(--logo-gold);
    font-size: 34px;
    line-height: 1.05;
    letter-spacing: 0.02em;
    text-transform: uppercase;
  }
  .logo-name span { display: block; }
  .logo-dot {
    width: 26px;
    height: 26px;
    border-radius: 50%;
    background: var(--logo-gold);
  }
  .divider {
    position: absolute;
    left: 0;
    top: 0;
  }
  .number-badge {
    position: absolute;
    left: 552px;
    top: 227px;
    width: 95px;
    height: 45px;
    background: var(--ink);
    border: 2px solid var(--ink);
    outline: 1.5px solid var(--number-gold);
    outline-offset: -5px;
    border-radius: 3px;
    display: flex;
    align-items: center;
    justify-content: center;
    font-family: "Rokkitt", serif;
    font-weight: 700;
    font-size: 36px;
    color: var(--number-gold);
    letter-spacing: 0.3em;
    padding-left: 0.3em;
    box-sizing: border-box;
  }
  .product-title {
    position: absolute;
    left: 0;
    width: 1200px;
    top: 280px;
    margin: 0;
    text-align: center;
    font-family: "Rokkitt", serif;
    font-weight: 700;
    font-size: 62px;
    line-height: 1;
    letter-spacing: 0.05em;
    word-spacing: 0.15em;
    color: var(--ink);
    transform: scaleX(0.82);
  }
  .material-label {
    position: absolute;
    left: 0;
    width: 1200px;
    top: 390px;
    margin: 0;
    text-align: center;
    font-family: "Montserrat", sans-serif;
    font-weight: 800;
    font-size: 15px;
    letter-spacing: 0.55em;
    padding-left: 0.55em;
    color: var(--ink);
  }
</style>
</head>
<body>
  <main class="card">
    <div class="card-frame"></div>

    <div class="logo-panel">
      <div class="logo-name"><span>Tide Hollow</span><span>Equestrian</span></div>
      <div class="logo-dot"></div>
    </div>

    <svg class="divider" width="1200" height="480" viewBox="0 0 1200 480">
      <g stroke="var(--ink)" fill="none" stroke-width="3">
        <line x1="280" y1="255" x2="535" y2="255"/>
        <line x1="665" y1="255" x2="920" y2="255"/>
        <line x1="280" y1="361" x2="520" y2="361"/>
        <line x1="680" y1="361" x2="920" y2="361"/>
        <line x1="464" y1="418" x2="735" y2="418" stroke-width="2"/>
        <circle cx="540" cy="256" r="5" stroke-width="2"/>
        <circle cx="661" cy="256" r="5" stroke-width="2"/>
        <circle cx="540" cy="362" r="5" stroke-width="2"/>
        <circle cx="661" cy="362" r="5" stroke-width="2"/>
      </g>
      <g fill="var(--ink)">
        <circle cx="276" cy="255" r="3.5"/>
        <circle cx="924" cy="255" r="3.5"/>
        <circle cx="276" cy="361" r="3.5"/>
        <circle cx="924" cy="361" r="3.5"/>
        <circle cx="464" cy="418" r="2.5"/>
        <circle cx="735" cy="418" r="2.5"/>
      </g>
      <rect role="img" aria-label="Decorative scroll flourish" x="552" y="354" width="96" height="16" rx="8" fill="var(--ornament-tone)"/>
      <rect role="img" aria-label="Decorative scroll flourish" x="576" y="422" width="48" height="28" rx="10" fill="var(--ornament-tone)"/>
    </svg>

    <div class="number-badge">123</div>

    <h1 class="product-title">Equestrian Number Holder</h1>

    <p class="material-label">Genuine Leather</p>
  </main>
</body>
</html>
```